we are a college and require a design of a printable graduation certificate

our courses range from certicate III to Diploma

We would a high quality design, similar to a unveristy degree, so its meaning full to the students and looks great on the wall

our college website is: www.marlowinstitute.example.au

Industry/Entity Type

College

Requirements
Must have
• security feature like water mark or stamp

```html
<!DOCTYPE html>
<html lang="en">
<head>
<meta charset="utf-8">
<title>Marlow Institute – Certificate of Graduation</title>
<link rel="stylesheet" href="https://fonts.googleapis.com/css2?family=Alegreya:ital,wght@1,400;1,500&family=Tinos:wght@700&display=swap">
<style>
  :root {
    --paper: #ffffdf;
    --lace: #8fa8f2;
    --lace-deep: #3d68e6;
    --gold: #9a6f2c;
    --ink: #161616;
    --title-blue: #2a5cf0;
    --crest: #2b57e4;
    --watermark: rgba(154, 111, 44, 0.09);
    --stamp: #9a6f2c;
  }
  * { margin: 0; padding: 0; box-sizing: border-box; }
  html, body { width: 1200px; height: 913px; overflow: hidden; background: var(--paper); }
  .certificate {
    position: relative;
    width: 1200px;
    height: 913px;
    background: var(--paper);
    font-family: "Alegreya", Georgia, serif;
    font-style: italic;
    color: var(--ink);
  }
  .lace-border {
    position: absolute;
    inset: 8px;
    border: 52px solid var(--lace);
    border-radius: 14px;
    box-shadow: inset 0 0 0 2px var(--lace-deep), 0 0 0 2px var(--lace-deep);
  }
  .security-watermark {
    position: absolute;
    left: 60px; top: 60px;
    width: 1080px; height: 793px;
    overflow: hidden;
    pointer-events: none;
  }
  .security-watermark text {
    font-family: "Tinos", "Times New Roman", serif;
    font-weight: 700;
    font-size: 30px;
    letter-spacing: 4px;
    fill: var(--watermark);
  }
  .college-arc {
    position: absolute;
    left: 0; top: 0;
    width: 1200px; height: 300px;
  }
  .college-arc text {
    font-family: "Alegreya", Georgia, serif;
    font-style: italic;
    font-size: 108px;
    fill: var(--gold);
  }
  .emblem {
    position: absolute;
    left: 550px; top: 230px;
    width: 100px; height: 100px;
    background: var(--crest);
  }
  .college-name {
    position: absolute;
    left: 0; width: 1200px; top: 386px;
    text-align: center;
    font-family: "Tinos", "Times New Roman", serif;
    font-style: normal;
    font-weight: 700;
    font-size: 30px;
    letter-spacing: 0.5px;
    color: var(--ink);
  }
  .address {
    position: absolute;
    left: 0; width: 1200px; top: 428px;
    text-align: center;
    font-size: 28px;
  }
  .certificate-title {
    position: absolute;
    left: 0; width: 1200px; top: 465px;
    text-align: center;
    font-size: 42px;
    font-weight: 400;
    color: var(--title-blue);
    letter-spacing: 1px;
  }
  .field {
    position: absolute;
    font-size: 27px;
    white-space: nowrap;
  }
  .field-name { left: 153px; top: 526px; }
  .field-dob { left: 684px; top: 526px; }
  .statement { left: 156px; top: 589px; }
  .field-marks { left: 153px; top: 638px; }
  .field-date { left: 778px; top: 638px; }
  .signatory { position: absolute; font-size: 27px; }
  .signatory-registrar { left: 175px; top: 694px; }
  .signatory-principal { left: 930px; top: 697px; }
  .signature-line { position: absolute; top: 760px; font-size: 27px; }
  .signature-registrar { left: 145px; }
  .signature-principal { left: 901px; }
  .security-stamp {
    position: absolute;
    left: 530px; top: 690px;
    width: 140px; height: 140px;
  }
  .security-stamp text {
    font-family: "Tinos", "Times New Roman", serif;
    font-weight: 700;
    font-size: 13px;
    letter-spacing: 2px;
    fill: var(--stamp);
  }
</style>
</head>
<body>
<main class="certificate">
  <div class="lace-border" role="img" aria-label="Decorative blue rosette lace border framing the certificate"></div>

  <svg class="security-watermark" viewBox="0 0 1080 793" aria-hidden="true">
    <g transform="rotate(-20 540 396)">
      <text x="-200" y="120">MARLOW INSTITUTE · MARLOW INSTITUTE · MARLOW INSTITUTE · MARLOW INSTITUTE</text>
      <text x="-320" y="260">MARLOW INSTITUTE · MARLOW INSTITUTE · MARLOW INSTITUTE · MARLOW INSTITUTE</text>
      <text x="-200" y="400">MARLOW INSTITUTE · MARLOW INSTITUTE · MARLOW INSTITUTE · MARLOW INSTITUTE</text>
      <text x="-320" y="540">MARLOW INSTITUTE · MARLOW INSTITUTE · MARLOW INSTITUTE · MARLOW INSTITUTE</text>
      <text x="-200" y="680">MARLOW INSTITUTE · MARLOW INSTITUTE · MARLOW INSTITUTE · MARLOW INSTITUTE</text>
      <text x="-320" y="820">MARLOW INSTITUTE · MARLOW INSTITUTE · MARLOW INSTITUTE · MARLOW INSTITUTE</text>
    </g>
  </svg>

  <svg class="college-arc" viewBox="0 0 1200 300" aria-label="Marlow Institute">
    <defs>
      <path id="college-arc-path" d="M 225 260 Q 600 30 1000 260"/>
    </defs>
    <text><textPath href="#college-arc-path" startOffset="50%" text-anchor="middle">Marlow Institute</textPath></text>
  </svg>

  <div class="emblem" aria-hidden="true"></div>
  <p class="college-name">MARLOW INSTITUTE</p>
  <p class="address">Level 2, 18 Carrow Lane, Kelvin Heights , Queensland 4059 , Australia</p>
  <h1 class="certificate-title">CERTIFICATE OF GRADUATION</h1>

  <p class="field field-name">Mr. / Ms. ..................................</p>
  <p class="field field-dob">Date of Birth .................................</p>
  <p class="field statement">has&nbsp; successfully passed Graduation Exams&nbsp; 2012.</p>
  <p class="field field-marks">Marks obtained&nbsp; .................%</p>
  <p class="field field-date">Date&nbsp; .................................</p>

  <p class="signatory signatory-registrar">Registrar</p>
  <p class="signatory signatory-principal">Principal</p>
  <p class="signature-line signature-registrar">........................</p>
  <p class="signature-line signature-principal">........................</p>

  <svg class="security-stamp" viewBox="0 0 140 140" role="img" aria-label="Official seal of Marlow Institute">
    <defs>
      <path id="stamp-ring" d="M 70 70 m -50 0 a 50 50 0 1 1 100 0 a 50 50 0 1 1 -100 0"/>
    </defs>
    <circle cx="70" cy="70" r="66" fill="none" stroke="var(--stamp)" stroke-width="3"/>
    <circle cx="70" cy="70" r="38" fill="none" stroke="var(--stamp)" stroke-width="1.5"/>
    <text><textPath href="#stamp-ring" startOffset="0">MARLOW INSTITUTE · OFFICIAL SEAL ·</textPath></text>
    <text x="70" y="75" text-anchor="middle">SEAL</text>
  </svg>
</main>
</body>
</html>
```